Power Point Template Kalvoren sustainability consulting

Please note:
We are not looking for new design proposals anymore since we've already received templetes from two designers that we really like. We are currently discussing possible changes with them and will make a final decision soon. Thank you very much.

(find english description below)
We are a small German start-up that offers sustainability consulting. For presentations of results, our company presentation, proposals, lectures, etc., we need a PowerPoint template that matches our logo. We come from classic management consulting / strategy consulting and also deal with facts and figures in sustainability consulting. Therefore, the template should not be too fancy and should not only consist of photos. But it shouldn't be a completely sober template either. Our logo with the green leaves for sustainability (three leaves for KALvoren) and the white bar chart (with the dynamic swing upwards) reflects our attitude well, where we see ourselves on the range from playful to sober and classic to modern.

It might be nice for the template to include the shape of one of the leaves (from the logo). Also, the logo should appear in a corner of each slide. The colors from the logo (see appendix) should be partially reflected in the presentation. We can also imagine a gold-brown tone (see website www.kalvoren-consulting.example) or a coral tone as a contrast. (Attention - the website is not final yet).

For a first suggestion, it is sufficient to suggest three to four slides (cover sheet, chapter/separation slide, text slide, data slide). We will then mark drafts that we like. In total, we would then need about 6-10 more slide templates, e.g. about us, team, slide for a statement, 2-3 data charts (pie, bar, column), top 3 - 5 list, timeline, contact (more slides are welcome ).

We are a small German start-up offering sustainability consulting. We need a power point template for result presentations, our company presentation, proposals, lectures etc. The template should be aligned with our logo. Our background lies in classic management consulting / strategy consulting and we also deal with facts and figures in sustainability consulting. Therefore, the template should not be too playful and not only consist of photos. But it should also not be a completely clear template. Our logo with the green leaves for sustainability (three leaves for KALvoren) and the white bar chart (with the dynamic upward swing) reflects our attitude well, where we see ourselves on the range from playful to down-to-earth and classic to modern .

For the template, it might be nice to incorporate the shape of one of the leaves (from the logo). Also, the logo should show up in one corner on each slide. Some of the colors from the logo (see attachment) should be reflected in the presentation. We could also think of a gold-brown tone (see website www.kalvoren-consulting.example) or a coral tone for contrast. (Attention - the website is not final yet).

For a first proposal it is quite sufficient to suggest us three to four slides (cover page, chapter/separation slide, text slide, data slide). We will then mark the drafts that we like. In total we would need about 6-10 more slide templates, eg About us, Team, slide for a statement, 2-3 data charts (pie, bar, column), Top 3 - 5 List, Timeline, Contact (more slides are welcome).

Target Market(s)

Corporations, large companies and SMEs

Industry/Entity Type

Unternehmensberatung, Nachhaltigkeitsberatung

Font styles to use
Sans Serif
Other font styles liked:
• Calibri

Colors
00AB8E
00BBA5
67D7C9
C6EFE9
E9F9F6

Requirements
Must have
• see description (e.g. the colors of our logo)
Nice to have
• see description (e.g. elements of the logo included)
Should not have
• see description

```html
<!DOCTYPE html>
<html lang="en">
<head>
<meta charset="utf-8">
<title>Kalvoren Consulting – Presentation Template</title>
<link rel="stylesheet" href="https://fonts.googleapis.com/css2?family=Lato:wght@400;700&family=Open+Sans:wght@400;700&display=swap">
<style>
:root{
  --canvas:#e9e7d2;
  --slide:#f4f4ef;
  --green-deep:#1e3a0a;
  --green-dark:#2e5e10;
  --green:#4a8a1c;
  --green-light:#8db83a;
  --lime:#a9cf5a;
  --lime-pale:#e3ebc4;
  --sage:#adc991;
  --ink:#2b2b2b;
  --grey:#4d5055;
}
*{box-sizing:border-box;margin:0;padding:0}
html,body{width:1200px;height:4149px;overflow:hidden;background:var(--canvas)}
body{position:relative;font-family:"Lato",sans-serif;color:var(--ink)}
.slide{position:absolute;left:44px;width:1112px;height:625px;background:var(--slide);overflow:hidden}
.footer{position:absolute;left:0;bottom:0;width:100%;height:26px;background:linear-gradient(90deg,var(--green) 0%,var(--green-dark) 100%);color:#fff;font-size:12px;display:flex;align-items:center;justify-content:space-between;padding:0 18px}
.footer .mail{display:flex;align-items:center;gap:10px}
.heading{position:absolute;left:18px;top:36px;font-family:"Open Sans",sans-serif;font-weight:700;font-size:36px;color:var(--green-dark);letter-spacing:.5px}
.heading::after{content:"";position:absolute;left:88px;right:-20px;bottom:-4px;height:2px;background:var(--green-light)}
.corner-brand{position:absolute;right:20px;top:44px;display:flex;align-items:center;gap:6px;font-family:"Lato",sans-serif;font-weight:700;font-size:15px;color:var(--green)}
.corner-brand i{width:14px;height:14px;border-radius:50%;background:var(--green);display:block}
.body-text{position:absolute;left:18px;width:538px;font-size:15px;line-height:26px;text-align:justify}
.body-text p+p{margin-top:10px}

/* cover */
.brand-name{position:absolute;left:0;width:100%;text-align:center;font-family:"Lato",sans-serif;font-weight:400;color:var(--grey)}
.cover .brand-name{top:262px;font-size:118px;line-height:1}
.brand-sub{position:absolute;left:0;width:100%;text-align:center;font-size:32px;letter-spacing:2px;color:var(--grey)}
.cover .brand-sub{top:396px}
.brand-dot{position:absolute;border-radius:50%;background:var(--green-light)}
.date-bar{position:absolute;left:283px;top:448px;width:546px;height:45px;background:var(--lime);border-radius:10px 30px 30px 10px;display:flex;align-items:center;justify-content:center;gap:10px;font-size:15px;color:var(--green-deep)}

/* about */
.offer{position:absolute;top:382px;width:110px;text-align:center}
.offer .badge{width:90px;height:90px;margin:0 auto;background:var(--green-light);border-radius:50% 4px 50% 4px;display:flex;align-items:center;justify-content:center}
.offer span{display:block;margin-top:28px;font-size:15px}
.photo-ring{position:absolute;border-radius:50%}

/* team */
.member{position:absolute;top:140px;width:250px;text-align:center}
.member .card{position:absolute;top:123px;left:0;width:250px;height:306px;background:#fff;border-radius:120px 120px 130px 130px;box-shadow:0 6px 18px rgba(0,0,0,.12)}
.member .portrait{position:relative;width:176px;height:176px;margin:0 auto;border-radius:50%;border:6px solid var(--green-light);background:radial-gradient(circle at 50% 45%,#c9a58f 0%,#8e6b58 45%,#3f3a37 100%)}
.member h3{position:relative;margin-top:30px;font-size:13px;font-weight:700;letter-spacing:.3px}
.member p{position:relative;margin:10px auto 0;width:200px;font-size:10.5px;line-height:20.6px}

/* timeline */
.year{position:absolute;top:359px;width:78px;height:78px;border-radius:50%;background:var(--green-deep);color:#fff;font-family:"Open Sans",sans-serif;font-weight:700;font-size:17px;display:flex;align-items:center;justify-content:center;box-shadow:10px 4px 0 var(--lime-pale)}
.milestone{position:absolute;width:190px;text-align:center}
.milestone h4{font-size:10.5px;font-weight:700;margin-bottom:6px}
.milestone p{font-size:10.5px;line-height:20.6px}

/* contact */
.contact-item{position:absolute;top:339px;width:240px;text-align:center}
.contact-item .icon{width:52px;height:52px;margin:0 auto;border-radius:50%;background:var(--green-deep);display:flex;align-items:center;justify-content:center}
.contact-item h4{margin-top:38px;font-size:13px;font-weight:700}
.contact-item p{font-size:13px;line-height:26px}
</style>
</head>
<body>

<!-- Slide 1: Cover -->
<section class="slide cover" style="top:55px">
  <span class="brand-dot" style="left:534px;top:200px;width:44px;height:44px"></span>
  <div class="brand-name">Kalvoren</div>
  <div class="brand-sub">CONSULTING</div>
  <div class="date-bar">
    <svg width="18" height="16" viewBox="0 0 18 16"><rect x="1" y="3" width="16" height="12" rx="1.5" fill="var(--green-deep)"/><rect x="4" y="0" width="2" height="5" fill="var(--green-deep)"/><rect x="12" y="0" width="2" height="5" fill="var(--green-deep)"/><rect x="3" y="7" width="12" height="1.5" fill="var(--lime)"/></svg>
    <span>04 January 2023</span>
  </div>
  <footer class="footer"><span class="mail"><svg width="16" height="11" viewBox="0 0 16 11"><rect width="16" height="11" rx="1" fill="#fff"/><path d="M0.5 0.8 8 6.5 15.5 0.8" stroke="var(--green)" stroke-width="1.4" fill="none"/></svg>info@kalvoren-consulting.example</span><span>01</span></footer>
</section>

<!-- Slide 2: About us -->
<section class="slide" style="top:735px">
  <h2 class="heading">ABOUT US</h2>
  <div class="corner-brand"><i></i>Kalvoren</div>
  <div class="body-text" style="top:150px">
    <p>At Kalvoren Consulting, we support companies and public institutions in anchoring and expanding sustainability in their companies – with the aim of making them more attractive, future-proof and successful.</p>
    <p>Regardless of whether you are still at the very beginning of the process of implementing sustainability aspects in your company or whether sustainable management is already anchored in the corporate culture - we will be happy to support you with our modular offers:</p>
  </div>
  <div class="offer" style="left:3px">
    <div class="badge"><svg width="44" height="44" viewBox="0 0 44 44" fill="#fff"><rect x="20" y="4" width="4" height="36"/><path d="M8 10h24l5 4-5 4H8z"/><path d="M36 22H14l-5 4 5 4h22z"/></svg></div>
    <span>Orientation</span>
  </div>
  <div class="offer" style="left:172px">
    <div class="badge"><svg width="44" height="44" viewBox="0 0 44 44" fill="#fff"><rect x="4" y="22" width="16" height="16"/><rect x="24" y="4" width="16" height="16"/><path d="M26 26l10 0-4-4M18 18l-10 0 4 4" stroke="#fff" stroke-width="3" fill="none"/></svg></div>
    <span>Strategy</span>
  </div>
  <div class="offer" style="left:341px">
    <div class="badge"><svg width="44" height="44" viewBox="0 0 44 44" fill="#fff"><circle cx="16" cy="16" r="11"/><circle cx="30" cy="30" r="10"/><circle cx="30" cy="30" r="4" fill="var(--green-light)"/></svg></div>
    <span>Implementation</span>
  </div>
  <span class="photo-ring" style="left:658px;top:90px;width:470px;height:470px;border:1.5px solid var(--green-light)"></span>
  <span class="photo-ring" style="left:680px;top:100px;width:440px;height:460px;background:var(--lime);opacity:.75"></span>
  <div class="photo-ring" role="img" aria-label="Photo of three consultants working together at a table with laptops in a bright office" style="left:686px;top:76px;width:440px;height:440px;background:radial-gradient(circle at 55% 40%,#e6e9ea 0%,#b9bfc2 45%,#5e6468 80%,#2f3236 100%)"></div>
  <footer class="footer"><span class="mail"><svg width="16" height="11" viewBox="0 0 16 11"><rect width="16" height="11" rx="1" fill="#fff"/><path d="M0.5 0.8 8 6.5 15.5 0.8" stroke="var(--green)" stroke-width="1.4" fill="none"/></svg>info@kalvoren-consulting.example</span><span>02</span></footer>
</section>

<!-- Slide 3: Team -->
<section class="slide" style="top:1413px">
  <h2 class="heading">OUR TEAM</h2>
  <div class="corner-brand"><i></i>Kalvoren</div>
  <article class="member" style="left:102px">
    <div class="card"></div>
    <div class="portrait" role="img" aria-label="Portrait photo of Dr Marlene Osterholt"></div>
    <h3>DR MARLENE OSTERHOLT</h3>
    <p>Marlene is co-founder and managing director of Kalvoren Consulting GmbH. She has a high level of analytical comprehension, thinks very far ahead and always keeps an overview of the essential issues. Marlene is passionate about the topic of sustainability and can easily inspire other people with her friendly nature.</p>
  </article>
  <article class="member" style="left:444px">
    <div class="card"></div>
    <div class="portrait" role="img" aria-label="Portrait photo of Dr Jana Wellbrock"></div>
    <h3>DR JANA WELLBROCK</h3>
    <p>Jana is co-founder and managing director of Kalvoren Consulting GmbH. She is very good at systematically grasping complex issues and reducing them to the essentials. She thinks with foresight and develops target group-oriented solutions with foresight.</p>
  </article>
  <article class="member" style="left:785px">
    <div class="card"></div>
    <div class="portrait" role="img" aria-label="Portrait photo of Dr Carla Brenninger-Voss"></div>
    <h3>DR CARLA BRENNINGER-VOSS</h3>
    <p>Carla is co-founder and managing director of Kalvoren Consulting GmbH. She always manages to react pragmatically and solution-oriented to changing customer requirements in dynamic project environments, without losing sight of the essentials.</p>
  </article>
  <footer class="footer"><span class="mail"><svg width="16" height="11" viewBox="0 0 16 11"><rect width="16" height="11" rx="1" fill="#fff"/><path d="M0.5 0.8 8 6.5 15.5 0.8" stroke="var(--green)" stroke-width="1.4" fill="none"/></svg>info@kalvoren-consulting.example</span><span>03</span></footer>
</section>

<!-- Slide 4: Data chart -->
<section class="slide" style="top:2093px">
  <h2 class="heading">DATA CHART</h2>
  <div class="corner-brand"><i></i>Kalvoren</div>
  <div class="body-text" style="top:160px">
    <p>Lorem ipsum dolor sit amet, consectetur adipiscing elit, sed do eiusmod tempor incididunt ut labore et dolore magna aliqua. Ut enim ad minim veniam, quis nostrud exercitation ullamco laboris nisi ut aliquip ex ea commodo consequat.</p>
    <p>Sed ut perspiciatis unde omnis iste natus error sit voluptatem accusantium doloremque laudantium, totam rem aperiam, eaque ipsa quae ab illo inventore veritatis et quasi architecto beatae vitae dicta sunt explicabo. Nemo enim ipsam voluptatem quia voluptas sit aspernatur aut odit aut fugit, sed quia consequuntur magni dolores eos qui ratione voluptatem sequi nesciunt. Neque porro quisquam est, qui dolorem ipsum quia dolor sit amet, consectetur, adipisci velit, sed quia non numquam eius modi tempora incidunt ut labore et dolore magnam aliquam quaerat voluptatem.</p>
  </div>
  <svg class="pie-chart" style="position:absolute;left:600px;top:60px" width="520" height="520" viewBox="-260 -259 520 520">
    <circle cx="18" cy="-12" r="234" fill="none" stroke="var(--green-light)" stroke-width="1.5"/>
    <circle cx="0" cy="-5" r="226" fill="var(--lime-pale)" opacity=".7"/>
    <circle cx="0" cy="8" r="198" fill="#000" opacity=".12"/>
    <path d="M0 0V-195A195 195 0 0 1 195 0Z" fill="var(--green)"/>
    <path d="M0 0H195A195 195 0 0 1 157.8 114.6Z" fill="var(--green-dark)"/>
    <path d="M0 0L157.8 114.6A195 195 0 0 1 -157.8 114.6Z" fill="var(--green-deep)"/>
    <path d="M0 0L-157.8 114.6A195 195 0 0 1 0 -195Z" fill="var(--green-light)"/>
    <g fill="#fff" font-family="Open Sans, sans-serif" font-weight="700" font-size="17" text-anchor="middle">
      <text x="79" y="-78">25%</text>
      <text x="-92" y="-31">35%</text>
      <text x="126" y="56">10%</text>
      <text x="5" y="119">30%</text>
    </g>
  </svg>
  <footer class="footer"><span class="mail"><svg width="16" height="11" viewBox="0 0 16 11"><rect width="16" height="11" rx="1" fill="#fff"/><path d="M0.5 0.8 8 6.5 15.5 0.8" stroke="var(--green)" stroke-width="1.4" fill="none"/></svg>info@kalvoren-consulting.example</span><span>04</span></footer>
</section>

<!-- Slide 5: Timeline -->
<section class="slide" style="top:2771px">
  <h2 class="heading">TIMELINE</h2>
  <div class="corner-brand"><i></i>Kalvoren</div>
  <div class="body-text" style="top:155px;width:1075px;text-align:left">
    <p>Lorem ipsum dolor sit amet, consectetur adipiscing elit, sed do eiusmod tempor incididunt ut labore et dolore magna aliqua. Ut enim ad minim veniam, quis nostrud exercitation ullamco laboris nisi ut aliquip ex ea commodo consequat.</p>
  </div>
  <div class="milestone" style="left:243px;top:242px"><h4>LOREM IPSUM</h4><p>Lorem ipsum dolor sit amet, consectetur adipiscing elit, sed do eiusmod tempor incididunt ut labore et dolore magna aliqua.</p></div>
  <div class="milestone" style="left:665px;top:242px"><h4>LOREM IPSUM</h4><p>Lorem ipsum dolor sit amet, consectetur adipiscing elit, sed do eiusmod tempor incididunt ut labore et dolore magna aliqua.</p></div>
  <div class="year" style="left:85px">2019</div>
  <div class="year" style="left:299px">2020</div>
  <div class="year" style="left:507px">2021</div>
  <div class="year" style="left:721px">2022</div>
  <div class="year" style="left:934px">2023</div>
  <svg style="position:absolute;left:0;top:370px" width="1112" height="40" viewBox="0 0 1112 40" fill="none" stroke="var(--grey)" stroke-width="1.2">
    <g stroke-dasharray="3 3"><path d="M188 24Q230 6 274 18"/><path d="M402 20Q440 34 486 22"/><path d="M610 24Q650 6 697 18"/><path d="M824 20Q862 34 910 22"/></g>
    <path d="M268 14l6 4-7 2M480 18l6 4-7 3M691 14l6 4-7 2M904 18l6 4-7 3"/>
  </svg>
  <div class="milestone" style="left:29px;top:450px"><h4>LOREM IPSUM</h4><p>Lorem ipsum dolor sit amet, consectetur adipiscing elit, sed do eiusmod tempor incididunt ut labore et dolore magna aliqua.</p></div>
  <div class="milestone" style="left:451px;top:450px"><h4>LOREM IPSUM</h4><p>Lorem ipsum dolor sit amet, consectetur adipiscing elit, sed do eiusmod tempor incididunt ut labore et dolore magna aliqua.</p></div>
  <div class="milestone" style="left:878px;top:450px"><h4>LOREM IPSUM</h4><p>Lorem ipsum dolor sit amet, consectetur adipiscing elit, sed do eiusmod tempor incididunt ut labore et dolore magna aliqua.</p></div>
  <footer class="footer"><span class="mail"><svg width="16" height="11" viewBox="0 0 16 11"><rect width="16" height="11" rx="1" fill="#fff"/><path d="M0.5 0.8 8 6.5 15.5 0.8" stroke="var(--green)" stroke-width="1.4" fill="none"/></svg>info@kalvoren-consulting.example</span><span>05</span></footer>
</section>

<!-- Slide 6: Contact -->
<section class="slide contact" style="top:3451px;background:var(--sage)">
  <span style="position:absolute;left:10px;top:-330px;width:1090px;height:1300px;border-radius:50%;background:#eef0e4"></span>
  <span class="brand-dot" style="left:534px;top:120px;width:44px;height:44px"></span>
  <div class="brand-name" style="top:176px;font-size:96px;line-height:1">Kalvoren</div>
  <div class="brand-sub" style="top:280px;font-size:26px">CONSULTING</div>
  <div class="contact-item" style="left:107px">
    <div class="icon"><svg width="22" height="26" viewBox="0 0 22 26" fill="none" stroke="#fff" stroke-width="1.8"><path d="M11 24S3 15 3 9.5a8 8 0 0 1 16 0C19 15 11 24 11 24Z"/><circle cx="11" cy="9.5" r="3"/></svg></div>
    <h4>ADDRESS:</h4>
    <p>Kalvoren Consulting GmbH<br>Lindenhof Business Park<br>Ahornweg 12<br>60311 Frankfurt am Main</p>
  </div>
  <div class="contact-item" style="left:339px">
    <div class="icon"><svg width="24" height="24" viewBox="0 0 24 24" fill="none" stroke="#fff" stroke-width="1.8"><path d="M5 2h4l2 5-3 2a12 12 0 0 0 7 7l2-3 5 2v4a2 2 0 0 1-2 2A19 19 0 0 1 3 4a2 2 0 0 1 2-2Z"/></svg></div>
    <h4>PHONE:</h4>
    <p>+49 (0) 69 – 555 0142</p>
  </div>
  <div class="contact-item" style="left:545px">
    <div class="icon"><svg width="26" height="20" viewBox="0 0 26 20" fill="none" stroke="#fff" stroke-width="1.8"><rect x="1" y="1" width="24" height="18" rx="2"/><path d="M1.5 2 13 11 24.5 2"/></svg></div>
    <h4>EMAIL:</h4>
    <p>info@kalvoren-consulting.example</p>
  </div>
  <div class="contact-item" style="left:797px">
    <div class="icon"><svg width="26" height="26" viewBox="0 0 26 26" fill="none" stroke="#fff" stroke-width="1.6"><circle cx="13" cy="13" r="11"/><ellipse cx="13" cy="13" rx="5" ry="11"/><path d="M2 13h22M4 7h18M4 19h18"/></svg></div>
    <h4>WEBSITE:</h4>
    <p>www.kalvoren-consulting.example</p>
  </div>
  <footer class="footer" style="justify-content:flex-end"><span>06</span></footer>
</section>

</body>
</html>
```